Design new RK Capital business card 2016

We need a new business card for our company RK Capital Stewardship. We are a niche Alternative Investment Fund Manager based in Chester, in the North West of the UK.We market our services to global institutions such as banks, insurance companies, pension funds, etc. as well as wealthy individuals. Our main markets are Europe (Germany\France\Switzerland), the US and parts of Asia.
The design needs to be in line with existing company branding. Life the assets we deal with, the business card might suggest, "niche\alternative" type of attributes - however, it needs to remain professional, clean and appropriate for our client base.
Our existing business card format with relevant factual information is included, along with logo and branding details.

Target Market(s)

We market our services to global institutions such as banks, insurance companies, pension funds, etc. as well as wealthy individuals.

Industry/Entity Type

Financial Service

Contact Information for Business Card

please see attached pdf for information on existing business card which we should aim to convey on your new design. However:
- the wording "RK Capital Stewardship Ltd is Authorised and Regulated
by the Monetary Oversight Bureau. Registered No. 7139604" should be replaced with , "RK Capital Stewardship Ltd is an Alternative Investment Fund Manager Authorised and Regulated by the Monetary Oversight Bureau. Registered No. 7139604"
- the "reception" word on reverse can be omitted.
- the "retail: www.marbowhill.co.uk" wording can be omitted.
- the QR code is not required in the new version.

Font styles to use
Serif
Sans Serif

Requirements
Must have
• information on current business card, subject to comments provided above.
Nice to have
• Use of areas of solid colour instead of large areas of white space might be nice to experiment with. However, still need to have the general look and feel of the brand as presented on our website www.rkcapfold.co.uk
• If we had space for 3 bullet points describing what we do\who we are, this might be good to try out. e.g. alternative investment fund manager, longevity specialist, founded 1990.
• Also, we have a new tag line, "wisdom built to endure" which might fit nicely somewhere on the business card.
Should not have
• - no QR code
• - should not use all the colours in our logo as it looks very garish! Using one or two colours with black\white etc, seems to work better.

```html
<!DOCTYPE html>
<html lang="en">
<head>
<meta charset="utf-8">
<title>RK Capital Stewardship – Business Card</title>
<link href="https://fonts.googleapis.com/css2?family=Crimson+Text:ital,wght@0,400;0,600;0,700;1,400&family=Open+Sans:ital,wght@0,400;1,400&display=swap" rel="stylesheet">
<style>
  :root {
    --brown: #5e3a12;
    --olive: #a39a0c;
    --ink: #2c2620;
    --grey-text: #5a534c;
    --card: #ffffff;
    --backdrop: #e8e4de;
  }
  * { box-sizing: border-box; margin: 0; padding: 0; }
  html, body {
    width: 1200px; height: 950px; overflow: hidden;
    background: var(--backdrop);
  }
  .sheet {
    position: relative; width: 1200px; height: 950px;
  }
  .card {
    position: absolute; left: 270px; width: 660px; height: 380px;
    background: var(--card);
    box-shadow: 0 6px 18px rgba(0,0,0,0.18);
    overflow: hidden;
  }
  .card--front { top: 70px; }
  .card--back { top: 500px; }

  .front-swoosh { position: absolute; inset: 0; width: 100%; height: 100%; }

  .holder {
    position: absolute; right: 245px; top: 40px; text-align: right;
  }
  .holder__name {
    font-family: "Crimson Text", serif; font-weight: 700;
    font-size: 30px; color: var(--brown); line-height: 1.1;
  }
  .holder__role {
    font-family: "Crimson Text", serif; font-weight: 400;
    font-size: 19px; color: var(--olive); margin-top: 2px;
  }

  .brand {
    position: absolute; left: 40px; top: 150px;
    display: flex; align-items: center; gap: 14px;
  }
  .brand__dot {
    width: 58px; height: 58px; border-radius: 50%;
    background: var(--olive);
  }
  .brand__name {
    font-family: "Crimson Text", serif; font-weight: 400;
    font-size: 26px; color: var(--brown);
  }

  .contact {
    position: absolute; left: 44px; top: 232px; list-style: none;
    font-family: "Open Sans", sans-serif; font-size: 13px; color: var(--grey-text);
  }
  .contact li { display: flex; align-items: center; gap: 9px; height: 20px; }
  .contact svg { width: 12px; height: 12px; fill: var(--grey-text); }

  .tagline {
    position: absolute; left: 44px; top: 322px;
    font-family: "Crimson Text", serif; font-weight: 700;
    font-size: 19px; color: var(--ink);
  }

  .back-brand {
    position: absolute; left: 0; right: 0; top: 70px;
    display: flex; flex-direction: column; align-items: center; gap: 14px;
  }
  .back-brand__dot {
    width: 120px; height: 120px; border-radius: 50%; background: var(--olive);
  }
  .back-brand__name {
    font-family: "Crimson Text", serif; font-weight: 400;
    font-size: 24px; color: var(--brown);
  }
  .credentials {
    position: absolute; left: 40px; right: 40px; bottom: 34px; text-align: center;
    font-family: "Open Sans", sans-serif; font-style: italic; color: var(--grey-text);
  }
  .credentials__points { font-size: 13.5px; }
  .credentials__rule {
    height: 1px; background: var(--brown); margin: 8px 30px;
  }
  .credentials__legal { font-size: 11.5px; line-height: 1.5; }
</style>
</head>
<body>
<main class="sheet">

  <section class="card card--front" aria-label="Business card front">
    <svg class="front-swoosh" viewBox="0 0 660 380" preserveAspectRatio="none" aria-hidden="true">
      <rect x="440" y="0" width="220" height="380" fill="var(--brown)"/>
      <path d="M0,0 L430,0 C585,55 635,235 555,380 L0,380 Z" fill="var(--card)"/>
      <path d="M430,0 C585,55 635,235 555,380 L598,380 C668,230 630,60 520,0 Z" fill="var(--olive)"/>
      <path d="M520,0 C630,60 668,230 598,380" fill="none" stroke="var(--card)" stroke-width="5"/>
    </svg>

    <div class="holder">
      <p class="holder__name">Martin Hale</p>
      <p class="holder__role">Non-Executive Chairman</p>
    </div>

    <div class="brand">
      <span class="brand__dot"></span>
      <span class="brand__name">RK Capital Stewardship</span>
    </div>

    <ul class="contact">
      <li><svg viewBox="0 0 12 12"><path d="M2.5 0.5 L4.5 0.5 L5.2 3.2 L3.8 4.2 C4.5 5.8 6 7.4 7.8 8.2 L8.8 6.8 L11.5 7.5 L11.5 9.5 C11.5 10.8 10.5 11.5 9.5 11.5 C4.5 11 1 7.5 0.5 2.5 C0.5 1.5 1.2 0.5 2.5 0.5 Z"/></svg>+44 (0)1632 960418</li>
      <li><svg viewBox="0 0 12 12"><path d="M3 0 H9 A1 1 0 0 1 10 1 V11 A1 1 0 0 1 9 12 H3 A1 1 0 0 1 2 11 V1 A1 1 0 0 1 3 0 Z M3.5 1.5 V9.5 H8.5 V1.5 Z"/></svg>+44 (0)7700 900562</li>
      <li><svg viewBox="0 0 12 12"><path d="M0 2 H12 V10 H0 Z M1 3 L6 6.5 L11 3 V3.2 L6 7.6 L1 3.2 Z" fill-rule="evenodd"/></svg>mhale@rkcapfold.co.uk</li>
      <li><svg viewBox="0 0 12 12"><circle cx="6" cy="6" r="5.5"/></svg>www.rkcapfold.co.uk</li>
    </ul>

    <p class="tagline">Wisdom built to endure</p>
  </section>

  <section class="card card--back" aria-label="Business card back">
    <div class="back-brand">
      <span class="back-brand__dot"></span>
      <span class="back-brand__name">RK Capital Stewardship</span>
    </div>
    <div class="credentials">
      <p class="credentials__points">Alternative Investment Fund Manager • Longevity Specialist • Founded 1990</p>
      <div class="credentials__rule"></div>
      <p class="credentials__legal">RK Capital Stewardship Ltd is an Alternative Investment Fund Manager Authorised and<br>Regulated by the Monetary Oversight Bureau. Registered No. 7139604</p>
    </div>
  </section>

</main>
</body>
</html>
```